indépendant en tant que Massothérapeute et Préparateur Mental, j'ai besoin de ...

Massothérapeute et préparateur mental indépendant, je recherche une carte de visite sobre et dynamique, sans images liées au massage ou à la préparation mentale mais intégrant mon logo. Les couleurs que j'aime bien sont : Blanc, gris, anthracite, noir et jaune

Contact Information for Business Card

carte de préférence Horizontale
neutre qui puisse toucher le deux domaines Massothérapie et préparation mentale

Requirements
Must have
• mon projet doit intégrer au recto:
LOGO
Loïc Vermande
078 315 26 49
info@loicvermande-exemple.ch
et éventuellement www.loicvermande-exemple.ch

et au verso les deux adresses:

Chemin des Ormelets 27B
1400 Yverdon-les-Bains

Rue des Tanneries 9
1700 Fribourg

Should not have
• mon projet ne doit pas contenir d'image en liens avec le massage ni la préparation mentale.

```html
<!DOCTYPE html>
<html lang="fr">
<head>
<meta charset="utf-8">
<title>Loïc Vermande – Cartes de visite</title>
<link rel="stylesheet" href="https://fonts.googleapis.com/css2?family=Lato:wght@400;700&display=swap">
<style>
  :root {
    --bg: #e4e4e4;
    --paper: #ffffff;
    --yellow: #fdc010;
    --ink: #111111;
    --rule: #c8c8c8;
  }
  * { margin: 0; padding: 0; box-sizing: border-box; }
  html, body { width: 1200px; height: 801px; overflow: hidden; }
  body {
    background: var(--bg);
    font-family: "Lato", sans-serif;
    color: var(--ink);
    position: relative;
  }
  .card {
    position: absolute;
    left: 354px;
    width: 520px;
    height: 312px;
    background: var(--paper);
    overflow: hidden;
  }
  .card--addresses { top: 43px; }
  .card--contact { top: 424px; }

  /* Address side */
  .frame-top, .frame-bottom, .frame-left { position: absolute; background: var(--yellow); }
  .frame-top { left: 0; top: 0; width: 260px; height: 18px; }
  .frame-bottom { left: 0; bottom: 0; width: 260px; height: 18px; }
  .frame-left { left: 0; top: 0; width: 18px; height: 312px; }

  .pin { position: absolute; left: 30px; top: 149px; width: 14px; height: 20px; }
  .address {
    position: absolute;
    top: 144px;
    font-size: 12.5px;
    line-height: 16px;
  }
  .address--yverdon { left: 51px; }
  .address--fribourg { left: 249px; }
  .address-slash { position: absolute; left: 229px; top: 145px; width: 14px; height: 28px; }
  .address-rule { position: absolute; left: 260px; top: 175px; width: 1px; height: 17px; background: var(--rule); }

  .brand-name-small {
    position: absolute;
    left: 396px;
    top: 152px;
    font-size: 11px;
    font-weight: 700;
  }
  .accent-tab { position: absolute; right: 0; top: 148px; width: 34px; height: 18px; background: var(--yellow); }

  /* Contact side */
  .brand {
    position: absolute;
    left: 40px;
    top: 145px;
    display: flex;
    align-items: center;
    gap: 10px;
  }
  .brand-mark { width: 14px; height: 14px; background: var(--yellow); }
  .brand-name { font-size: 22px; font-weight: 700; }

  .divider { position: absolute; left: 260px; top: 100px; width: 1px; height: 120px; background: var(--rule); }

  .person-name {
    position: absolute;
    left: 289px;
    top: 104px;
    font-size: 19px;
    font-weight: 700;
    letter-spacing: 0.3px;
  }
  .contact-list {
    position: absolute;
    left: 292px;
    top: 144px;
    list-style: none;
    font-size: 13.5px;
    line-height: 22px;
    letter-spacing: 0.2px;
  }
  .contact-list b { display: inline-block; width: 14px; font-weight: 700; }

  .bar-yellow { position: absolute; left: 0; bottom: 0; width: 409px; height: 9px; background: var(--yellow); }
  .bar-black { position: absolute; left: 411px; bottom: 0; width: 109px; height: 9px; background: var(--ink); }
</style>
</head>
<body>

<section class="card card--addresses">
  <div class="frame-top"></div>
  <div class="frame-left"></div>
  <div class="frame-bottom"></div>

  <svg class="pin" viewBox="0 0 14 20" aria-hidden="true">
    <path d="M7 0C3.1 0 0 3.1 0 7c0 5.2 7 13 7 13s7-7.8 7-13C14 3.1 10.9 0 7 0zm0 9.6A2.6 2.6 0 1 1 7 4.4a2.6 2.6 0 0 1 0 5.2z" fill="#111"/>
  </svg>
  <p class="address address--yverdon">Chemin des Ormelets 27B<br>1400 Yverdon-les-Bains</p>
  <svg class="address-slash" viewBox="0 0 14 28" aria-hidden="true">
    <line x1="13" y1="1" x2="1" y2="27" stroke="#555" stroke-width="1"/>
  </svg>
  <p class="address address--fribourg">Rue des Tanneries 9<br>1700 Fribourg</p>
  <div class="address-rule"></div>

  <span class="brand-name-small">Loïc Vermande</span>
  <div class="accent-tab"></div>
</section>

<section class="card card--contact">
  <div class="brand">
    <span class="brand-mark"></span>
    <span class="brand-name">Loïc Vermande</span>
  </div>

  <div class="divider"></div>

  <h1 class="person-name">Loïc Vermande</h1>
  <ul class="contact-list">
    <li><b>M</b> : 078 315 26 49</li>
    <li><b>E</b> : info@loicvermande-exemple.ch</li>
    <li><b>W</b> : www.loicvermande-exemple.ch</li>
  </ul>

  <div class="bar-yellow"></div>
  <div class="bar-black"></div>
</section>

</body>
</html>
```